Social Action Network Needs Banner Ads for Cause T-Shirts

Lend a Hand is a social action network that transforms ordinary internet actions into donations to non-profit organizations fighting for a better tomorrow. Users can donate their social influence, print coupons, accept free offers or shop online and every action benefits causes they love. You can watch a video here: http://www.lendahandhub.example/

We are about to launch a line of cause tees that benefit the various causes we support. We want the banner ads to be positive, uplifting, inspiring and attractive. We want the ads to incorporate the following wording (although, we encourage creativity): Dress better so others can live better.

We require typical banner ad sizes: 300 x 250, 160 x 600, 728 x 90 (more sizes would be much appreciated).

Please try to include the Lend a Hand logo (color can be changed based on ad design).

In case it helps, here is a link to a page we have set up for one of our partner charities: http://www.lendahandhub.example/BrightWellFund

Target Market(s)

While 80% of our users are women, we need to appeal to both.

Industry/Entity Type

Non-Profit

Requirements
Must have
• Lend a Hand logo and T-shirt design (with or without model). Also, some sort of call to action button - get tees, take action, buy now, check it out, learn more, etc.
Nice to have
• Feature the woman's tees and if possible the man's tees could be somewhere smaller in the background (if design allows).

```html
<!DOCTYPE html>
<html lang="en">
<head>
<meta charset="utf-8">
<title>Lend a Hand – Cause Tees Banner 300x250</title>
<link rel="stylesheet" href="https://fonts.googleapis.com/css2?family=Open+Sans:ital,wght@0,400;0,700;0,800;1,700&display=swap">
<style>
  :root {
    --page-light: #ffffff;
    --page-edge: #b9b9b9;
    --banner-border: #1a1a1a;
    --purple-deep: #8a00b8;
    --purple-bright: #d400f0;
    --headline-white: #ffffff;
    --headline-cyan: #27c6f2;
    --outline-black: #000000;
    --band-light: #f4f4f4;
    --band-mid: #d6d6d6;
    --accent-blue: #1c8fc4;
    --button-top: #36c0ee;
    --button-bottom: #0a7fb8;
    --logo-ink: #2a2a2a;
  }
  html, body {
    margin: 0;
    width: 1200px;
    height: 1000px;
    overflow: hidden;
  }
  body {
    background: radial-gradient(ellipse at center, var(--page-light) 0%, var(--page-light) 45%, var(--page-edge) 100%);
    position: relative;
    font-family: "Open Sans", sans-serif;
  }
  .banner {
    position: absolute;
    left: 458px;
    top: 351px;
    width: 298px;
    height: 248px;
    border: 1px solid var(--banner-border);
    overflow: hidden;
    box-shadow: 0 0 40px 12px rgba(0,0,0,0.35);
  }
  .banner__backdrop {
    position: absolute;
    inset: 0 0 55px 0;
    background: linear-gradient(160deg, var(--purple-bright) 0%, var(--purple-deep) 55%, var(--purple-bright) 100%);
  }
  .banner__model {
    position: absolute;
    left: 140px;
    top: 0;
    width: 158px;
    height: 195px;
    background: linear-gradient(180deg, #3a2a2a 0%, #1f9be0 25%, #1787c9 70%, #222 100%);
  }
  .headline {
    position: absolute;
    left: 0;
    top: 14px;
    width: 154px;
    text-align: center;
    font-weight: 800;
    color: var(--headline-white);
    text-shadow:
      -2px -2px 0 var(--outline-black), 2px -2px 0 var(--outline-black),
      -2px 2px 0 var(--outline-black), 2px 2px 0 var(--outline-black),
      0 2px 0 var(--outline-black), 0 -2px 0 var(--outline-black),
      2px 0 0 var(--outline-black), -2px 0 0 var(--outline-black);
  }
  .headline__line {
    display: block;
    font-size: 24px;
    line-height: 30px;
  }
  .headline__line--accent {
    color: var(--headline-cyan);
    font-size: 19px;
    line-height: 28px;
  }
  .footer-band {
    position: absolute;
    left: 0;
    bottom: 0;
    width: 298px;
    height: 66px;
  }
  .brand {
    position: absolute;
    left: 6px;
    bottom: 6px;
    display: flex;
    align-items: center;
    gap: 6px;
  }
  .brand__mark {
    width: 44px;
    height: 44px;
    border-radius: 50%;
    border: 3px solid var(--logo-ink);
    box-sizing: border-box;
    background: var(--band-light);
  }
  .brand__name {
    font-size: 19px;
    font-weight: 400;
    color: var(--logo-ink);
    letter-spacing: -0.3px;
  }
  .cta {
    position: absolute;
    left: 176px;
    bottom: 12px;
    width: 114px;
    height: 30px;
    border-radius: 4px;
    background: linear-gradient(180deg, var(--button-top), var(--button-bottom));
    box-shadow: 2px 3px 3px rgba(0,0,0,0.55);
    color: #fff;
    font-size: 16px;
    font-weight: 700;
    font-style: italic;
    text-align: center;
    line-height: 30px;
    text-decoration: none;
    text-shadow: 0 1px 1px rgba(0,0,0,0.5);
  }
</style>
</head>
<body>
  <div class="banner">
    <div class="banner__backdrop"></div>
    <div class="banner__model" role="img" aria-label="Woman wearing a blue V-neck cause tee with a script slogan print"></div>

    <div class="headline">
      <span class="headline__line">DRESS</span>
      <span class="headline__line">BETTER</span>
      <span class="headline__line headline__line--accent">so others can</span>
      <span class="headline__line">LIVE</span>
      <span class="headline__line">BETTER</span>
    </div>

    <svg class="footer-band" viewBox="0 0 298 66" width="298" height="66" aria-hidden="true">
      <defs>
        <linearGradient id="band-fill" x1="0" y1="0" x2="0" y2="1">
          <stop offset="0" stop-color="#f4f4f4"/>
          <stop offset="1" stop-color="#d0d0d0"/>
        </linearGradient>
      </defs>
      <path d="M0 8 Q149 18 298 6 L298 66 L0 66 Z" fill="url(#band-fill)"/>
      <path d="M0 8 Q149 18 298 6" fill="none" stroke="#1c8fc4" stroke-width="3"/>
    </svg>

    <div class="brand">
      <span class="brand__mark"></span>
      <span class="brand__name">Lend a Hand</span>
    </div>

    <a class="cta" href="http://www.lendahandhub.example/">Get Tees</a>
  </div>
</body>
</html>
```